construction company offering modern and striking homes and apartments

I need a card design for my new construction company called Talmont Constructions (vic) Pty Ltd.
We build everything from multi home development sites to modern and edgy apartment complexes.
I am open to any colors used as long as it stands out and doesn't look cheap. I want the final design to show my prospective clients I am a professional construction company

Industry/Entity Type

Construction

```html
<!DOCTYPE html>
<html lang="en">
<head>
<meta charset="utf-8">
<title>Talmont Constructions – Business Card</title>
<link href="https://fonts.googleapis.com/css2?family=Open+Sans:wght@400;600&display=swap" rel="stylesheet">
<style>
  :root {
    --stage: #2b2b2d;
    --card-light: #f4f4f4;
    --card-dark: #1d1b1c;
    --ink: #1b1b1b;
    --ink-soft: #3a3a3a;
    --paper-text: #e6e6e6;
    --muted: #bdbdbd;
    --rule: #9a9a9a;
    --gold: #d9a521;
    --badge-blue: #12306b;
    --badge-cream: #e9dfb0;
    --badge-green: #0f6b43;
  }
  * { box-sizing: border-box; margin: 0; padding: 0; }
  html, body { width: 1200px; height: 900px; overflow: hidden; }
  body {
    background: var(--stage);
    font-family: "Open Sans", sans-serif;
    position: relative;
  }
  .card {
    position: absolute;
    left: 320px;
    width: 560px;
    height: 320px;
    border-radius: 4px;
    overflow: hidden;
    box-shadow: 0 10px 30px rgba(0,0,0,.45);
  }
  .card-front { top: 95px; background: var(--card-light); }
  .card-back { top: 475px; background: var(--card-dark); color: var(--paper-text); }

  .brand { position: absolute; display: flex; align-items: center; gap: 16px; }
  .brand-mark { border-radius: 50%; flex: none; }
  .brand-name {
    font-weight: 400;
    text-transform: uppercase;
    letter-spacing: 1.5px;
    line-height: 1.05;
    font-size: 21px;
  }
  .card-front .brand { left: 130px; top: 110px; }
  .card-front .brand-mark { width: 100px; height: 100px; background: var(--ink); }
  .card-front .brand-name { color: var(--ink-soft); }

  .card-back .brand { left: 42px; top: 76px; }
  .card-back .brand-mark { width: 76px; height: 76px; border: 2px solid var(--paper-text); }
  .card-back .brand-name { color: var(--paper-text); font-size: 18px; }

  .membership { position: absolute; right: 36px; top: 26px; display: flex; align-items: flex-end; gap: 10px; }
  .membership-label { font-size: 11px; letter-spacing: .5px; text-transform: uppercase; color: var(--paper-text); text-align: right; margin-bottom: 4px; }
  .badge-row { display: flex; }
  .badge-seal { width: 40px; height: 30px; background: var(--badge-cream); }
  .badge-bar { width: 96px; height: 30px; background: var(--badge-blue); }
  .badge-square { width: 58px; height: 58px; border-radius: 10px; background: var(--badge-green); }

  .person { position: absolute; left: 42px; bottom: 32px; }
  .person-name { color: var(--gold); font-size: 21px; font-weight: 400; line-height: 1.2; }
  .person-role { color: var(--muted); font-size: 14px; margin-bottom: 10px; }
  .person-address { color: var(--muted); font-size: 15px; line-height: 1.35; font-style: normal; }

  .contact { position: absolute; left: 268px; bottom: 40px; padding-left: 16px; border-left: 2px solid var(--rule); }
  .contact-group { list-style: none; margin-bottom: 10px; }
  .contact-group:last-child { margin-bottom: 0; }
  .contact-group li { display: flex; align-items: center; gap: 9px; font-size: 12.5px; line-height: 1.5; color: var(--paper-text); white-space: nowrap; }
  .icon { width: 12px; height: 12px; flex: none; fill: var(--gold); }
</style>
</head>
<body>

<section class="card card-front" aria-label="Card front">
  <div class="brand">
    <span class="brand-mark"></span>
    <p class="brand-name">Talmont<br>Constructions</p>
  </div>
</section>

<section class="card card-back" aria-label="Card back">
  <div class="membership">
    <div>
      <p class="membership-label">Member of</p>
      <div class="badge-row" role="img" aria-label="Builders association membership badge">
        <span class="badge-seal"></span><span class="badge-bar"></span>
      </div>
    </div>
    <span class="badge-square" role="img" aria-label="Housing industry membership badge"></span>
  </div>

  <div class="brand">
    <span class="brand-mark"></span>
    <p class="brand-name">Talmont<br>Constructions</p>
  </div>

  <div class="person">
    <h1 class="person-name">Daniel Marsh</h1>
    <p class="person-role">managing director</p>
    <address class="person-address">48 Harbour Lane<br>Eastvale, Victoria 3150</address>
  </div>

  <div class="contact">
    <ul class="contact-group">
      <li>
        <svg class="icon" viewBox="0 0 16 16" aria-hidden="true"><path d="M4 0h8a1 1 0 0 1 1 1v14a1 1 0 0 1-1 1H4a1 1 0 0 1-1-1V1a1 1 0 0 1 1-1zm1 2v10h6V2zm3 11a1 1 0 1 0 0 2 1 1 0 0 0 0-2z"/></svg>
        03 9461 2075
      </li>
      <li>
        <svg class="icon" viewBox="0 0 16 16" aria-hidden="true"><path d="M4 0h8v5H4zM1 6h14a1 1 0 0 1 1 1v6h-3v3H3v-3H0V7a1 1 0 0 1 1-1zm4 5v3h6v-3z"/></svg>
        03 9461 2076
      </li>
    </ul>
    <ul class="contact-group">
      <li>
        <svg class="icon" viewBox="0 0 16 16" aria-hidden="true"><path d="M0 3h16v1.2L8 9 0 4.2zm0 2.6 8 4.8 8-4.8V13H0z"/></svg>
        dmarsh@talmontconstructions.com
      </li>
      <li>
        <svg class="icon" viewBox="0 0 16 16" aria-hidden="true"><path d="M8 0a8 8 0 1 0 0 16A8 8 0 0 0 8 0zm5.9 7h-2.5a12 12 0 0 0-1-4.6A6 6 0 0 1 13.9 7zM8 2c.7 1 1.3 2.8 1.4 5H6.6C6.7 4.8 7.3 3 8 2zM5.6 2.4A12 12 0 0 0 4.6 7H2.1a6 6 0 0 1 3.5-4.6zM2.1 9h2.5a12 12 0 0 0 1 4.6A6 6 0 0 1 2.1 9zM8 14c-.7-1-1.3-2.8-1.4-5h2.8C9.3 11.2 8.7 13 8 14zm2.4-.4a12 12 0 0 0 1-4.6h2.5a6 6 0 0 1-3.5 4.6z"/></svg>
        www.talmontconstructions.com
      </li>
    </ul>
  </div>
</section>

</body>
</html>
```